Vantoralis 'Private Prism' Book Cover Design project

I need to revise the book cover design I have for my coming book. The design I created through CraftHerd is great but the book has grown and changed so I'm looking for an alternative/option design. I can then choose later from the different options.

I need a book cover that represents the unique book I am creating.

Book Title:
Your True Spectrum

Subtitle: Walking Your Path and Not Your Tag

The book is targeting all readers with a special focus on same sex attracted readers. It should not have stereotypical images.

I am including a file of the book cover I have had designed. The back cover blurb, author info and author pic will remain the same. The colouring of the back cover and spine will, of course, change to match the colouring of the front cover.

The new title will be on the spine and the new title wording.

The front cover will be markedly different using the bold images and rainbow colours of the images found in the files I am uploading for you.

I am thinking of a large boldly coloured rainbow face with the title and subtitle ON the image. The image will be the whole cover. It will fill the cover as much as possible with the text added onto the pic.

The bold pictures I am including will give you the idea of what I'm looking for.

ANY of the images I've uploaded can be used as the actual front cover image OR the designer might have/find some suitable image to be used. The image is to be large and bold and fill the cover. Hopefully a positive energy.
It needs to be eye-catching and striking and bold and positive.

So...the book cover sample file I've provided can keep the back cover with completely new colouring. The front cover is completely new with new image, wording and energy.

It is to be a rainbow coloured face or figure for the cover image.

I hope that is clear enough for you. I'm very happy to discuss and clarify these ideas with the designer. Looking forward to another great CraftHerd experience.

Target Market(s)

Wide audience with special focus on Same Sex Attracted individuals

Font styles to use
Script
Other font styles liked:
• Some form of handwriting font to make the book title and text appear more personal....as if handwritten by me.

Requirements
Must have
• Boldness, Quirky, Rainbow Colour, Image to fill the cover, maybe dark cover contrasting background.
Nice to have
• A well balanced back cover especially in the area where the barcode will be placed.
Should not have
• No stereotypical images

```html
<!DOCTYPE html>
<html lang="en">
<head>
<meta charset="utf-8">
<title>Your True Spectrum — Book Cover</title>
<link rel="stylesheet" href="https://fonts.googleapis.com/css2?family=Montserrat:wght@400;500&family=Mr+Dafoe&display=swap">
<style>
  :root {
    --page: #ffffff;
    --ink: #ffffff;
    --paper: #f6f5f8;
    --magenta: #d6218f;
    --violet: #6a2a9c;
    --cobalt: #2a4fb8;
    --coral: #f2603a;
    --sun: #f4c63a;
    --teal: #3bb7c9;
  }
  * { box-sizing: border-box; margin: 0; padding: 0; }
  html, body {
    width: 1200px;
    height: 1200px;
    overflow: hidden;
    background: var(--page);
  }
  .canvas {
    position: relative;
    width: 1200px;
    height: 1200px;
    background: var(--page);
  }
  .cover {
    position: absolute;
    left: 250px;
    top: 75px;
    width: 700px;
    height: 1050px;
    overflow: hidden;
    background: var(--paper);
    box-shadow: 0 10px 30px rgba(40, 20, 60, 0.18);
  }
  .cover-art {
    position: absolute;
    inset: 0;
    background:
      radial-gradient(ellipse 70% 55% at 72% 38%, var(--magenta) 0%, rgba(214,33,143,0.85) 30%, rgba(106,42,156,0.55) 60%, rgba(246,245,248,0) 85%),
      radial-gradient(ellipse 90% 60% at 55% 95%, var(--cobalt) 0%, var(--violet) 40%, rgba(242,96,58,0.6) 70%, rgba(246,245,248,0) 95%),
      linear-gradient(160deg, var(--paper) 0%, var(--paper) 30%, rgba(59,183,201,0.35) 55%, rgba(244,198,58,0.45) 75%, var(--violet) 100%);
  }
  .author {
    position: absolute;
    left: 200px;
    top: 205px;
    font-family: "Montserrat", sans-serif;
    font-weight: 400;
    font-size: 33px;
    letter-spacing: 1px;
    color: var(--ink);
  }
  .title {
    position: absolute;
    left: 95px;
    top: 600px;
    width: 540px;
    font-family: "Mr Dafoe", cursive;
    font-weight: 400;
    color: var(--ink);
    line-height: 0.9;
    transform: rotate(-9deg);
    transform-origin: left top;
  }
  .title-top {
    display: flex;
    align-items: baseline;
    gap: 28px;
    margin-left: 70px;
  }
  .title-small { font-size: 92px; }
  .title-mid { font-size: 140px; }
  .title-large { display: block; font-size: 132px; margin-top: -10px; }
  .subtitle {
    position: absolute;
    left: 110px;
    top: 885px;
    width: 560px;
    font-family: "Montserrat", sans-serif;
    font-weight: 500;
    font-size: 31px;
    letter-spacing: 4px;
    line-height: 1.15;
    text-transform: uppercase;
    text-align: center;
    color: var(--ink);
    transform: rotate(-14deg);
  }
</style>
</head>
<body>
  <main class="canvas">
    <section class="cover">
      <div class="cover-art" role="img" aria-label="Photograph of a bearded man in profile, head and shoulders covered in vivid rainbow powder paint with colour splashes on a white background"></div>
      <p class="author">COLM ASHDOWN</p>
      <h1 class="title">
        <span class="title-top">
          <span class="title-small">Your</span>
          <span class="title-mid">True</span>
        </span>
        <span class="title-large">Spectrum</span>
      </h1>
      <p class="subtitle">Walking your path and<br>not your tag</p>
    </section>
  </main>
</body>
</html>
```